"Green Shopper Award" sales presentation

UK: "Shopper Award Green" is a French label, rewarding the best organic product sold in hyper and supermarkets. We already did the presentation in PPT format. But it is not design and professional-looking enough. The idea is that you use the existing document, and do not change anything in the structure, content, and text: you only have to improve the design (using the appropriate color code). We thank you in advance for any suggestion! FR: "Palme Acheteurs Vert" is a French distinction that rewards the best organic products sold in supermarkets and hypermarkets. The sales pitch is already done in PPT version. However, he still does not look pretty design / professional. Thus, we do not want you to modify the content, the structure, the images, but simply that you make it more design (following the appropriate graphic). Thank you in advance for your feedback!

Target Market(s)

Organic brands and supermarkets / organic brands and supermarkets

Requirements
Must have
• Follow the structure of the PPT made available (see attachment), keep the structure and the content, but improve the design - ideally with illustrator Ideally use Illustrator (Adobe) to improve the design of the current presentation - purpose keep the same content and structure
Nice to have
• You can use Illustrator ideally (or photoshop) to rework the design of the PPT

```html
<!DOCTYPE html>
<html lang="fr">
<head>
<meta charset="utf-8">
<title>Palme Acheteurs Vert 2019 – Présentation commerciale</title>
<link rel="stylesheet" href="https://fonts.googleapis.com/css2?family=Montserrat:wght@500;600;700;800&family=Open+Sans:wght@400;600;700&display=swap">
<style>
:root{
  --pink:#e5177b;
  --pink-soft:#f7c6dc;
  --teal:#1c6e7b;
  --green:#8cbf2b;
  --green-dark:#5f9a2a;
  --grey:#8a8a8a;
  --text:#6b6b6b;
  --white:#ffffff;
}
*{box-sizing:border-box;margin:0;padding:0}
html,body{width:800px;height:1200px;overflow:hidden;background:var(--white)}
body{font-family:"Open Sans",Arial,sans-serif;color:var(--text);position:relative}
.icon-defs{position:absolute;width:0;height:0;overflow:hidden}
.slide{position:absolute;width:392px;height:220px;background:var(--white);overflow:hidden;box-shadow:0 1px 4px rgba(0,0,0,.12)}
.col-l{left:4px}.col-r{left:404px}
.row-1{top:10px}.row-2{top:250px}.row-3{top:490px}.row-4{top:730px}.row-5{top:970px}
.slide::after{content:"";position:absolute;left:0;right:0;bottom:0;height:34px;background:linear-gradient(180deg,rgba(255,255,255,0),rgba(205,225,175,.45));pointer-events:none}
.cover::after,.closing::after{display:none}
.slide-title{position:absolute;left:15px;top:10px;font-family:"Montserrat",sans-serif;font-weight:600;font-size:14px;color:var(--teal)}
.title-rule{position:absolute;left:15px;top:31px;width:18px;height:2px;background:var(--pink)}
.page-num{position:absolute;left:18px;bottom:6px;font-size:5px;color:var(--grey);z-index:2}
.foot{position:absolute;right:12px;bottom:7px;display:flex;gap:8px;align-items:center;z-index:2}
.mark-client{display:flex;align-items:center;gap:3px;font-family:"Montserrat",sans-serif;font-weight:700;font-size:5px;color:var(--pink)}
.mark-client i{width:8px;height:8px;background:var(--pink);display:block}
.mark-agency{display:flex;align-items:center;gap:3px;font-family:"Montserrat",sans-serif;font-weight:700;font-size:5px;color:var(--teal)}
.mark-agency i{width:8px;height:8px;border-radius:50%;border:1.5px solid var(--green);display:block}
.ph{position:absolute}
.body-txt{position:absolute;font-size:4.3px;line-height:1.35;color:var(--text)}
.body-txt b{color:#444}
.icon-ring,.icon-disc{position:absolute;width:28px;height:28px;border-radius:50%;display:flex;align-items:center;justify-content:center}
.icon-ring{border:1.5px solid var(--pink);color:var(--pink)}
.icon-disc{background:var(--pink);color:#fff;font-family:"Montserrat",sans-serif;font-weight:700;font-size:7px;box-shadow:0 0 0 3px var(--pink-soft)}
.icon-ring svg,.icon-disc svg{width:15px;height:15px}
.lead{font-family:"Montserrat",sans-serif;font-weight:700;font-size:5.5px;color:var(--pink)}

/* cover */
.cover-photo{position:absolute;left:0;top:0;width:392px;height:178px}
.cover-wave{position:absolute;left:0;top:120px;width:392px;height:100px}
.cover-title{position:absolute;font-family:"Montserrat",sans-serif;font-weight:800;line-height:1.08;text-transform:uppercase}
.cover-brands{position:absolute;left:26px;top:166px;display:flex;gap:20px;align-items:center}
.cover-brands .mark-client{font-size:8px}
.cover-brands .mark-client i{width:20px;height:20px}
.cover-brands .mark-agency{font-size:10px;letter-spacing:.5px}
.cover-brands .mark-agency i{width:18px;height:18px;border-width:2.5px}

/* sommaire */
.toc{position:absolute;left:16px;top:64px;list-style:none}
.toc li{display:flex;align-items:center;height:15.5px;font-size:6.2px;color:var(--text)}
.toc li span{font-family:"Montserrat",sans-serif;font-weight:700;font-size:9px;color:var(--pink-soft);width:16px}
.brands-box{position:absolute;left:196px;top:69px;width:180px;height:101px;border:1px solid var(--pink-soft);border-radius:4px}
.brands-head{background:var(--pink);color:#fff;font-family:"Montserrat",sans-serif;font-weight:600;font-size:6.2px;text-align:center;padding:4px 0}
.brands-grid{display:grid;grid-template-columns:repeat(4,1fr);gap:5px;padding:8px}
.brand{height:28px;border:1px solid #ececec;border-radius:3px;display:flex;align-items:center;justify-content:center;text-align:center;font-weight:700;font-size:5px;color:var(--green-dark)}

/* mini screens */
.mini-card{position:absolute;background:#fff;border:1px solid #dedede;box-shadow:0 1px 3px rgba(0,0,0,.12);padding:3px}
.mini-card .bar{height:2.5px;margin:2.5px 0;border-radius:1px}

/* timeline */
.tl-line{position:absolute;left:14px;top:117px;width:360px;height:2px;background:#e3e3e3}
.tl-dot{position:absolute;top:110px;width:15px;height:15px;border-radius:50%;background:var(--pink);color:#fff;font-family:"Montserrat",sans-serif;font-weight:700;font-size:6.5px;display:flex;align-items:center;justify-content:center;border:2px solid #fff;box-shadow:0 0 0 1px var(--pink-soft)}
.tl-date{position:absolute;font-size:3.6px;color:var(--grey);transform:rotate(-90deg);transform-origin:left top;white-space:nowrap}
.tl-head{font-weight:700;color:var(--pink);font-size:4.3px}

/* participer panels */
.panel{position:absolute;display:flex;color:#fff}
.panel-label{width:56px;display:flex;align-items:center;justify-content:center;font-family:"Montserrat",sans-serif;font-weight:700;font-size:6.2px}
.panel ul{list-style:none;padding:6px 6px 0 0;font-size:4.2px;line-height:1.3}
.panel li{margin-bottom:3px;padding-left:7px;position:relative}
.panel li::before{content:"";position:absolute;left:0;top:1px;width:3.5px;height:3.5px;border:.8px solid #fff;border-radius:1px}

/* visibility */
.vis-label{position:absolute;font-size:4.3px;line-height:1.35;color:var(--pink);font-weight:700}
.fair-name{position:absolute;font-family:"Montserrat",sans-serif;font-weight:700;font-size:7px;color:#333;white-space:nowrap}

/* closing */
.closing-photo{position:absolute;left:0;top:60px;width:392px;height:160px}
.closing .brands-top{position:absolute;left:16px;top:20px;display:flex;gap:28px;align-items:center}
.closing .brands-top .mark-client{font-size:9px}
.closing .brands-top .mark-client i{width:28px;height:28px}
.closing .brands-top .mark-agency{font-size:13px;letter-spacing:.6px}
.closing .brands-top .mark-agency i{width:22px;height:22px;border-width:3px}
</style>
</head>
<body>

<svg class="icon-defs" aria-hidden="true">
  <defs>
    <symbol id="i-people" viewBox="0 0 24 24" fill="none" stroke="currentColor" stroke-width="1.6" stroke-linecap="round"><circle cx="12" cy="7" r="2.6"/><path d="M7.5 19v-3a4.5 4.5 0 0 1 9 0v3"/><circle cx="5" cy="9" r="2"/><path d="M1.5 19v-2a3.5 3.5 0 0 1 4.5-3.3"/><circle cx="19" cy="9" r="2"/><path d="M22.5 19v-2a3.5 3.5 0 0 0-4.5-3.3"/></symbol>
    <symbol id="i-shelf" viewBox="0 0 24 24" fill="none" stroke="currentColor" stroke-width="1.6"><rect x="3" y="3" width="18" height="18" rx="1"/><path d="M3 12h18"/><path d="M6 6v4M9 6v4M12 6v4M15 6v4M6 15v4M10 15v4M14 15v4M18 15v4"/></symbol>
    <symbol id="i-clipboard" viewBox="0 0 24 24" fill="none" stroke="currentColor" stroke-width="1.6" stroke-linecap="round"><rect x="5" y="4" width="14" height="17" rx="1.5"/><rect x="9" y="2.5" width="6" height="3" rx="1"/><path d="M8 10l1 1 2-2M13 10h4M8 15l1 1 2-2M13 15h4"/></symbol>
    <symbol id="i-medal" viewBox="0 0 24 24" fill="none" stroke="currentColor" stroke-width="1.6" stroke-linejoin="round"><circle cx="12" cy="9.5" r="6"/><circle cx="12" cy="9.5" r="3"/><path d="M8.5 14.5L6.5 22l3-1.5L11 22M15.5 14.5l2 7.5-3-1.5L13 22"/></symbol>
    <symbol id="i-network" viewBox="0 0 24 24" fill="none" stroke="currentColor" stroke-width="1.6"><circle cx="12" cy="5" r="2.5"/><circle cx="5" cy="18" r="2.5"/><circle cx="19" cy="18" r="2.5"/><path d="M12 7.5V12M5 15.5V12h14v3.5"/></symbol>
    <symbol id="i-doc" viewBox="0 0 24 24" fill="none" stroke="currentColor" stroke-width="1.6" stroke-linecap="round"><path d="M6 2.5h8l4 4V21.5H6z"/><path d="M14 2.5v4h4"/><path d="M9 18v-3M12 18v-5M15 18v-7"/></symbol>
    <symbol id="i-cart" viewBox="0 0 24 24" fill="none" stroke="currentColor" stroke-width="1.6" stroke-linecap="round" stroke-linejoin="round"><path d="M2 4h3l2.5 11h11l2-8H6.5"/><circle cx="9" cy="19.5" r="1.6"/><circle cx="17" cy="19.5" r="1.6"/></symbol>
    <symbol id="i-tag" viewBox="0 0 24 24" fill="none" stroke="currentColor" stroke-width="1.6" stroke-linejoin="round"><path d="M3 3h9l9 9-9 9-9-9z"/><circle cx="8" cy="8" r="1.6"/></symbol>
    <symbol id="i-megaphone" viewBox="0 0 24 24" fill="none" stroke="currentColor" stroke-width="1.6" stroke-linejoin="round"><path d="M3 10v4h4l9 5V5L7 10z"/><path d="M19 9a4 4 0 0 1 0 6"/></symbol>
    <symbol id="i-trophy" viewBox="0 0 24 24" fill="none" stroke="currentColor" stroke-width="1.6" stroke-linejoin="round"><path d="M7 3h10v5a5 5 0 0 1-10 0z"/><path d="M7 5H4a3 3 0 0 0 3 4M17 5h3a3 3 0 0 1-3 4M12 13v4M8 21h8l-1-4H9z"/></symbol>
    <symbol id="i-screen" viewBox="0 0 24 24" fill="none" stroke="currentColor" stroke-width="1.6" stroke-linecap="round"><rect x="2.5" y="4" width="19" height="13" rx="1"/><path d="M9 21h6M12 17v4M6 8h7M6 11h10"/></symbol>
    <symbol id="i-search" viewBox="0 0 24 24" fill="none" stroke="currentColor" stroke-width="1.8" stroke-linecap="round"><circle cx="10" cy="10" r="6"/><path d="M14.5 14.5L20 20"/></symbol>
    <symbol id="i-news" viewBox="0 0 24 24" fill="none" stroke="currentColor" stroke-width="1.6" stroke-linecap="round"><rect x="3" y="4" width="18" height="16" rx="1"/><rect x="6" y="7" width="5" height="5"/><path d="M13 8h5M13 11h5M6 15h12M6 17.5h12"/></symbol>
    <symbol id="i-box" viewBox="0 0 24 24" fill="none" stroke="currentColor" stroke-width="1.6" stroke-linejoin="round"><path d="M3 7l9-4 9 4v10l-9 4-9-4z"/><path d="M3 7l9 4 9-4M12 11v10"/></symbol>
  </defs>
</svg>

<!-- Slide 1 : cover -->
<section class="slide cover col-l row-1">
  <div class="cover-photo" role="img" aria-label="Champ de blé doré au soleil, en flou" style="background:radial-gradient(ellipse at 70% 20%,#fbf1dc 0%,rgba(251,241,220,0) 55%),linear-gradient(160deg,#c99a5c 0%,#e3c08c 35%,#f1dcb4 60%,#d8aa6e 100%)"></div>
  <svg class="cover-wave" viewBox="0 0 392 100" preserveAspectRatio="none" aria-hidden="true">
    <path d="M0 62 C90 18 200 72 392 6 L392 100 L0 100Z" fill="#fff"/>
    <path d="M130 58 C230 60 300 30 392 12" fill="none" stroke="var(--teal)" stroke-width="2"/>
  </svg>
  <div class="cover-title" style="right:18px;top:56px;text-align:right;font-size:17px;color:#93b84a">Palme<br>Acheteurs Vert<br>2019</div>
  <div class="cover-brands">
    <span class="mark-client"><i></i>Palme Acheteurs Vert 2019</span>
    <span class="mark-agency"><i></i>VERDANTA</span>
  </div>
</section>

<!-- Slide 2 : cover variant -->
<section class="slide cover col-r row-1">
  <div class="cover-photo" role="img" aria-label="Champ vert sous un ciel turquoise" style="background:linear-gradient(180deg,#1f7c83 0%,#3f9a6f 45%,#8cbf4a 80%,#b6d470 100%)"></div>
  <svg class="cover-wave" viewBox="0 0 392 100" preserveAspectRatio="none" aria-hidden="true">
    <path d="M0 70 C120 40 250 70 392 20 L392 100 L0 100Z" fill="#fff"/>
  </svg>
  <div class="cover-title" style="left:24px;top:46px;font-size:19px;color:#fff">Palme<br>Acheteurs Vert<br>2019</div>
  <div class="cover-brands">
    <span class="mark-client"><i></i>Palme Acheteurs Vert 2019</span>
    <span class="mark-agency"><i></i>VERDANTA</span>
  </div>
</section>

<!-- Slide 3 : sommaire -->
<section class="slide col-l row-2">
  <h2 class="slide-title">Sommaire</h2><div class="title-rule"></div>
  <ol class="toc">
    <li><span>01</span>Palme Acheteurs Vert, c'est quoi?</li>
    <li><span>02</span>Une certification d'excellence</li>
    <li><span>03</span>Qui peut concourir?</li>
    <li><span>04</span>Le déroulement du concours</li>
    <li><span>05</span>Participer, c'est...</li>
    <li><span>06</span>La visibilité des lauréats</li>
    <li><span>07</span>Inscription</li>
  </ol>
  <div class="brands-box">
    <div class="brands-head">Les marques participantes de l'édition 2018</div>
    <div class="brands-grid">
      <div class="brand">Rucher Doré</div><div class="brand">Plein Champ</div><div class="brand">Terre Claire</div><div class="brand">Four Vert</div>
      <div class="brand">Potager Net</div><div class="brand">Belle Prairie</div><div class="brand">Sève Pure</div><div class="brand">Miel de Lune</div>
    </div>
  </div>
  <div class="page-num">3</div>
  <div class="foot"><span class="mark-client"><i></i>PAV</span><span class="mark-agency"><i></i>VERDANTA</span></div>
</section>

<!-- Slide 4 : c'est quoi -->
<section class="slide col-r row-2">
  <h2 class="slide-title">Palme Acheteurs Vert, c'est quoi?</h2><div class="title-rule"></div>
  <div class="icon-ring" style="left:20px;top:60px"><svg><use href="#i-medal"/></svg></div>
  <p class="body-txt" style="left:58px;top:62px;width:100px">Ce concours distingue les produits bio et les produits écologiques les mieux notés du circuit GMS, afin d'encourager l'excellence dans ce secteur et aiguiller les consommateurs dans leurs achats.</p>
  <div class="icon-ring" style="left:20px;top:108px"><svg><use href="#i-network"/></svg></div>
  <p class="body-txt" style="left:58px;top:114px;width:100px">C'est la distinction de consommateurs réservée aux produits bio commercialisés en GMS (Grande et Moyenne Surface).</p>
  <div class="icon-ring" style="left:20px;top:156px"><svg><use href="#i-doc"/></svg></div>
  <p class="body-txt" style="left:58px;top:158px;width:100px">Elle permet d'identifier les produits d'excellence de la filière biologique en circuit GMS, les mettre en avant et stimuler leurs ventes et augmenter leur notoriété.</p>
  <div class="icon-ring" style="left:210px;top:60px"><svg><use href="#i-medal"/></svg></div>
  <p class="body-txt" style="left:246px;top:62px;width:130px">La distinction est calquée sur le même modèle que notre distinction des meilleurs produits, qui est elle dédiée au circuit spécialisé. Cette dernière, lancée en 2013, est très largement plébiscitée par les consommateurs.</p>
  <div class="mini-card" style="left:250px;top:104px;width:70px;height:52px">
    <div class="bar" style="background:var(--pink);width:100%;height:4px;margin-top:0"></div>
    <div class="bar" style="background:#7fb0d6;width:85%"></div>
    <div class="bar" style="background:#7fb0d6;width:70%"></div>
    <div class="bar" style="background:#7fb0d6;width:62%"></div>
    <div class="bar" style="background:#7fb0d6;width:48%"></div>
    <div class="bar" style="background:#7fb0d6;width:35%"></div>
    <div class="bar" style="background:#7fb0d6;width:22%"></div>
  </div>
  <div class="ph" style="left:312px;top:98px;width:20px;height:22px;background:var(--pink);border-radius:3px"></div>
  <p class="body-txt" style="left:250px;top:160px;width:90px;font-size:3.4px;color:var(--grey)">Enquête de notoriété, décembre 2017</p>
  <div class="page-num">4</div>
  <div class="foot"><span class="mark-client"><i></i>PAV</span><span class="mark-agency"><i></i>VERDANTA</span></div>
</section>

<!-- Slide 5 : certification -->
<section class="slide col-l row-3">
  <h2 class="slide-title">Une certification d'excellence</h2><div class="title-rule"></div>
  <div class="icon-disc" style="left:18px;top:52px"><svg><use href="#i-people"/></svg></div>
  <p class="body-txt" style="left:58px;top:56px;width:118px"><b>Un jury garanti indépendant</b> de 100 testeurs par produit (1500 testeurs au total) pour assurer le caractère représentatif des résultats.</p>
  <div class="icon-disc" style="left:18px;top:100px"><svg><use href="#i-clipboard"/></svg></div>
  <p class="body-txt" style="left:58px;top:102px;width:118px">Les produits <b>testés en situation réelle</b> par des consommateurs experts les ayant choisis (pas d'influence donc comme dans les laboratoires de tests ou les réunions consommateurs).</p>
  <div class="icon-disc" style="left:18px;top:148px">15/20</div>
  <p class="body-txt" style="left:58px;top:150px;width:118px">Une <b>note minimale de 15/20</b> est nécessaire pour prétendre à être lauréat (contre 11/20 pour d'autres distinctions du milieu conventionnel), et si deux produits sont en <b>concurrence directe</b>, seul le mieux noté des deux sera récompensé.</p>
  <div class="icon-disc" style="left:204px;top:52px"><svg><use href="#i-shelf"/></svg></div>
  <p class="body-txt" style="left:242px;top:56px;width:128px">Seuls <b>10% des produits</b> d'un <b>linéaire</b> peuvent être distingués (Ex: un rayon chocolats de 40 produits, si 10 produits concourent, seul 4 produits sur les 10 pourront être distingués).</p>
  <div class="icon-disc" style="left:204px;top:100px"><svg><use href="#i-medal"/></svg></div>
  <p class="body-txt" style="left:242px;top:102px;width:128px"><b>L'exploitation du logo est gratuite</b>, ce qui assure la crédibilité et <b>l'impartialité</b> de la distinction. Verdanta ne touche aucune rémunération quel que soit le produit gagnant ou perdant.</p>
  <div class="page-num">5</div>
  <div class="foot"><span class="mark-client"><i></i>PAV</span><span class="mark-agency"><i></i>VERDANTA</span></div>
</section>

<!-- Slide 6 : qui peut concourir -->
<section class="slide col-r row-3">
  <h2 class="slide-title">Qui peut concourir?</h2><div class="title-rule"></div>
  <div class="icon-disc" style="left:20px;top:50px"><svg><use href="#i-cart"/></svg></div>
  <p class="body-txt" style="left:58px;top:52px;width:100px"><span class="lead">Circuit GMS</span><br>Pour participer il est nécessaire que les produits présentés ne soient vendus qu'en <b>circuit GMS</b>.</p>
  <div class="icon-disc" style="left:20px;top:94px"><svg><use href="#i-tag"/></svg></div>
  <p class="body-txt" style="left:58px;top:96px;width:100px"><span class="lead">Marques indépendantes</span><br>Les marques indépendantes et les MDD peuvent désormais participer au concours.</p>
  <div class="ph" role="img" aria-label="Assortiment de produits bio : pots, boîtes, sachets et bouteilles" style="left:20px;top:138px;width:215px;height:66px;border-radius:3px;background:linear-gradient(90deg,#e9d3a6 0%,#d49a4a 18%,#f0e1c2 30%,#e6a83c 45%,#c98a5a 58%,#efe2c4 70%,#b7c86a 82%,#d9b48c 100%)"></div>
  <div class="icon-disc" style="left:206px;top:52px"><svg><use href="#i-medal"/></svg></div>
  <p class="body-txt" style="left:242px;top:54px;width:138px"><span class="lead">Produits labellisés</span><br>Cette distinction est uniquement destinée à des <b>produits labellisés</b>. Les labels retenus sont les suivants : label bio européen, labels biodynamiques, labels équitables, labels cosmétiques et labels écologiques reconnus.</p>
  <svg class="ph" style="left:242px;top:100px" width="130" height="16" aria-hidden="true">
    <g fill="none" stroke="#9bbf6a" stroke-width="1.2">
      <rect x="1" y="2" width="12" height="12"/><circle cx="26" cy="8" r="6"/><circle cx="44" cy="8" r="6"/><rect x="56" y="2" width="12" height="12" fill="#9bbf6a"/>
    </g>
    <rect x="74" y="4" width="18" height="8" fill="#f08a3c"/>
    <ellipse cx="106" cy="8" rx="8" ry="5" fill="none" stroke="#9bbf6a" stroke-width="1.2"/>
  </svg>
  <div class="page-num">6</div>
  <div class="foot"><span class="mark-client"><i></i>PAV</span><span class="mark-agency"><i></i>VERDANTA</span></div>
</section>

<!-- Slide 7 : déroulement -->
<section class="slide col-l row-4">
  <h2 class="slide-title">Le déroulement du concours</h2><div class="title-rule"></div>
  <div class="tl-line"></div>
  <div class="tl-dot" style="left:10px">1</div>
  <div class="tl-dot" style="left:54px">2</div>
  <div class="tl-dot" style="left:111px">3</div>
  <div class="tl-dot" style="left:172px">4</div>
  <div class="tl-dot" style="left:233px">5</div>
  <div class="tl-dot" style="left:294px">6</div>
  <span class="tl-date" style="left:20px;top:162px">Novembre - Mai</span>
  <span class="tl-date" style="left:64px;top:94px">Juin</span>
  <span class="tl-date" style="left:122px;top:165px">Septembre</span>
  <span class="tl-date" style="left:182px;top:96px">Fin Octobre</span>
  <span class="tl-date" style="left:243px;top:165px">Décembre</span>
  <span class="tl-date" style="left:304px;top:96px">Année Suivante</span>
  <div class="ph" role="img" aria-label="Photo de consommateurs choisissant des produits" style="left:60px;top:43px;width:42px;height:28px;background:linear-gradient(135deg,#f2e6da 0%,#d9a98a 45%,#b8785e 70%,#efe3d6 100%)"></div>
  <p class="body-txt" style="left:106px;top:43px;width:60px;font-size:3.9px"><span class="tl-head">Sélection des testeurs</span><br>1500 consommateurs de bio sont en tout sélectionnés pour tester des produits qu'ils choisissent.</p>
  <div class="mini-card" style="left:180px;top:39px;width:40px;height:28px;padding:2px">
    <svg width="34" height="22" viewBox="0 0 34 22" aria-hidden="true">
      <rect x="0" y="0" width="34" height="4" fill="#cfcfcf"/>
      <g stroke="#e2e2e2" stroke-width=".6"><path d="M0 8h34M0 12h34M0 16h34M0 20h34M12 4v18M23 4v18"/></g>
      <rect x="14" y="9" width="7" height="2" fill="var(--pink)"/><rect x="25" y="13" width="6" height="2" fill="var(--green)"/>
    </svg>
  </div>
  <p class="body-txt" style="left:224px;top:39px;width:60px;font-size:3.9px"><span class="tl-head">Réception des résultats</span><br>Selon des critères de notation précis par catégorie (goût, praticité, odeur...).</p>
  <div class="ph" style="left:300px;top:38px;width:24px;height:26px;background:var(--pink);border-radius:3px"></div>
  <p class="body-txt" style="left:328px;top:38px;width:52px;font-size:3.9px"><span class="tl-head">Utilisation de la distinction</span><br>Exploitation gratuite du logo pendant 1 an (du 1er janvier au 31 décembre).</p>
  <div class="ph" role="img" aria-label="Photo d'un testeur recevant un colis de produits" style="left:120px;top:160px;width:42px;height:28px;background:linear-gradient(135deg,#f4ede4 0%,#e0c4a0 50%,#b98d62 75%,#f0e6da 100%)"></div>
  <p class="body-txt" style="left:166px;top:160px;width:60px;font-size:3.9px"><span class="tl-head">Envoi des produits<br>Phase de test</span><br>Les consommateurs reçoivent les produits et les testent chez eux en situation réelle. Pas d'influence possible.</p>
  <div class="ph" role="img" aria-label="Photo de la cérémonie de remise des trophées" style="left:240px;top:146px;width:42px;height:28px;background:linear-gradient(135deg,#4e3f33 0%,#9a7f62 50%,#d8c2a2 100%)"></div>
  <p class="body-txt" style="left:286px;top:144px;width:92px;font-size:3.9px"><span class="tl-head">Cérémonie de remise des trophées</span><br>La soirée de remise des trophées de l'édition 2018 a accueilli la société de mesure et analyse des données. Réseau autour d'une discussion sur le bio en GMS et d'un repas bio au sein de l'Hôtel Belvédère.</p>
  <div class="page-num">7</div>
  <div class="foot"><span class="mark-client"><i></i>PAV</span><span class="mark-agency"><i></i>VERDANTA</span></div>
</section>

<!-- Slide 8 : participer (1) -->
<section class="slide col-r row-4">
  <h2 class="slide-title">Participer, c'est...</h2><div class="title-rule"></div>
  <div class="ph" role="img" aria-label="Salle de réception lors de la soirée" style="left:15px;top:46px;width:90px;height:64px;background:linear-gradient(160deg,#efe7da 0%,#bfa98c 40%,#7a6654 75%,#d9cbb5 100%)"></div>
  <div class="ph" role="img" aria-label="Pots de pâte à tartiner en test" style="left:108px;top:46px;width:60px;height:64px;background:radial-gradient(circle at 30% 30%,#e8c48e 0,#8b5a32 40%,transparent 41%),radial-gradient(circle at 75% 70%,#e8c48e 0,#7a4a28 38%,transparent 39%),linear-gradient(135deg,#5b3a22,#a8794c)"></div>
  <div class="ph" role="img" aria-label="Invités attablés pendant le dîner" style="left:15px;top:114px;width:90px;height:60px;background:linear-gradient(180deg,#d8cbb8 0%,#9d8a73 45%,#f2ece2 75%,#8e7b66 100%)"></div>
  <div class="ph" role="img" aria-label="Lauréats recevant leurs trophées" style="left:108px;top:114px;width:60px;height:60px;background:linear-gradient(135deg,#2f4a2e 0%,#6f8a55 45%,#cfd6bd 80%,#4d5a44 100%)"></div>
  <div class="panel" style="left:171px;top:46px;width:205px;height:80px;background:var(--pink)">
    <div class="panel-label" style="flex-direction:column;gap:4px"><svg width="16" height="16" style="opacity:.55"><use href="#i-clipboard"/></svg>PARTICIPANTS</div>
    <ul>
      <li><b>Test produit</b> réalisé auprès d'un panel de 100 consommateurs en affinité avec votre produit.</li>
      <li>Obtenir des <b>retours consommateurs</b> (téléchargement des verbatims) afin d'évaluer la perception de vos produits.</li>
      <li>Les produits sont présentés lors d'une <b>campagne de communication</b> et de <b>communiqués de presse</b> liés à l'opération.</li>
      <li>Présence à la <b>soirée de remise des trophées</b>.</li>
    </ul>
  </div>
  <div class="panel" style="left:171px;top:130px;width:205px;height:44px;background:linear-gradient(90deg,#8cbf2b,#a8c43a)">
    <div class="panel-label" style="flex-direction:column;font-size:5.5px"><span style="font-size:4px;margin-bottom:6px">Et en plus...</span>LAURÉATS</div>
    <ul style="padding-top:4px;font-size:3.8px">
      <li>Être identifié comme un produit bio bon et efficace : les consommateurs deviennent prescripteurs.</li>
      <li>Donner une valeur ajoutée et des arguments de vente à vos commerciaux et distributeurs.</li>
      <li>Un trophée avec le rappel du produit en inclusion dans du plexiglas.</li>
    </ul>
  </div>
  <div class="page-num">8</div>
  <div class="foot"><span class="mark-client"><i></i>PAV</span><span class="mark-agency"><i></i>VERDANTA</span></div>
</section>

<!-- Slide 9 : participer (2) visibilité -->
<section class="slide col-l row-5">
  <h2 class="slide-title">Participer, c'est...</h2><div class="title-rule"></div>
  <svg class="ph" style="left:120px;top:42px" width="150" height="140" viewBox="0 0 150 140" aria-hidden="true">
    <circle cx="75" cy="70" r="46" fill="none" stroke="var(--pink)" stroke-width="5"/>
    <circle cx="75" cy="70" r="38" fill="#fff" stroke="var(--pink-soft)" stroke-width="2"/>
    <g fill="#fff" stroke="var(--pink)" stroke-width="3">
      <circle cx="52" cy="30" r="14"/><circle cx="98" cy="30" r="14"/>
      <circle cx="121" cy="70" r="14"/><circle cx="98" cy="110" r="14"/>
      <circle cx="52" cy="110" r="14"/><circle cx="29" cy="70" r="14"/>
    </g>
    <g color="#e5177b">
      <use href="#i-box" x="44" y="22" width="16" height="16"/>
      <use href="#i-megaphone" x="90" y="22" width="16" height="16"/>
      <use href="#i-trophy" x="113" y="62" width="16" height="16"/>
      <use href="#i-screen" x="90" y="102" width="16" height="16"/>
      <use href="#i-news" x="44" y="102" width="16" height="16"/>
      <use href="#i-search" x="21" y="62" width="16" height="16"/>
    </g>
    <text x="75" y="56" text-anchor="middle" font-family="Montserrat,sans-serif" font-weight="700" font-size="5" fill="#e5177b">
      <tspan x="75">Visibilité accrue</tspan><tspan x="75" dy="6">des lauréats</tspan><tspan x="75" dy="6">grâce à une</tspan><tspan x="75" dy="6">campagne de</tspan><tspan x="75" dy="6">communication</tspan><tspan x="75" dy="6">complète</tspan>
    </text>
  </svg>
  <div class="ph" role="img" aria-label="Présentoir en magasin avec produits lauréats" style="left:56px;top:45px;width:30px;height:36px;background:linear-gradient(180deg,#2b2b2b 0 18%,#e9c7a0 18% 45%,#c9d89a 45% 70%,#3a3a3a 70%)"></div>
  <div class="ph" style="left:92px;top:46px;width:22px;height:22px;background:var(--pink);border-radius:3px"></div>
  <p class="vis-label" style="left:92px;top:70px;width:40px">En magasin<br>(stop-rayon...)</p>
  <p class="vis-label" style="left:46px;top:120px;width:76px">Mise en avant des lauréats 2019 lors du salon Organica Fair</p>
  <div class="fair-name" style="left:50px;top:137px">ORGANICA FAIR <span style="color:var(--pink)">2019</span></div>
  <p class="vis-label" style="left:96px;top:160px">Réseaux sociaux</p>
  <div class="ph" style="left:100px;top:170px;width:11px;height:11px;border-radius:50%;background:var(--pink)"></div>
  <div class="ph" style="left:114px;top:170px;width:11px;height:11px;border-radius:50%;background:var(--pink)"></div>
  <p class="vis-label" style="left:250px;top:48px">Relation presse<br>toute l'année</p>
  <div class="ph" role="img" aria-label="Photo de la cérémonie des trophées" style="left:282px;top:70px;width:34px;height:34px;border-radius:50%;background:radial-gradient(circle at 40% 35%,#e6dac6,#9a8568 55%,#4f4234)"></div>
  <p class="vis-label" style="left:284px;top:108px">Cérémonie de remise<br>des trophées</p>
  <p class="vis-label" style="left:248px;top:146px">Sites Internet<br>et newsletters dédiées</p>
  <div class="mini-card" style="left:250px;top:162px;width:32px;height:22px;padding:2px">
    <div class="bar" style="background:var(--pink);height:3px;margin:0 0 2px"></div>
    <div class="bar" style="background:var(--green);width:60%;margin:1.5px 0"></div>
    <div class="bar" style="background:#d4d4d4;margin:1.5px 0"></div>
    <div class="bar" style="background:#d4d4d4;width:80%;margin:1.5px 0"></div>
  </div>
  <p class="body-txt" style="left:286px;top:167px;width:92px;font-size:3.6px">Site internet dédié www.palme-vert.example<br>Campagne de pub sur www.verdanta.example</p>
  <div class="page-num">9</div>
  <div class="foot"><span class="mark-client"><i></i>PAV</span><span class="mark-agency"><i></i>VERDANTA</span></div>
</section>

<!-- Slide 10 : closing -->
<section class="slide closing col-r row-5">
  <div class="closing-photo" role="img" aria-label="Champ vert lumineux" style="background:linear-gradient(180deg,#3f8f7a 0%,#5fa25e 45%,#96c24c 80%,#bcd56a 100%)"></div>
  <svg class="ph" style="left:0;top:50px" width="392" height="60" viewBox="0 0 392 60" preserveAspectRatio="none" aria-hidden="true">
    <path d="M0 0 L392 0 L392 14 C280 10 150 60 0 46 Z" fill="#fff"/>
  </svg>
  <div class="brands-top">
    <span class="mark-client"><i></i>Palme Acheteurs Vert 2019</span>
    <span class="mark-agency"><i></i>VERDANTA</span>
  </div>
  <div class="ph" style="right:18px;top:98px;text-align:right;color:#fff">
    <div style="font-family:Montserrat,sans-serif;font-weight:500;font-size:15px">Participer, c'est...</div>
    <div style="font-size:6.5px;margin-top:4px">Date limite d'inscription des produits:</div>
    <div style="font-family:Montserrat,sans-serif;font-weight:700;font-size:15px;margin-top:2px">le 10 Juillet 2019</div>
  </div>
  <div class="ph" style="left:15px;top:164px;width:80px;border-bottom:1px solid rgba(255,255,255,.7);font-weight:700;font-size:6px;color:#fff;padding-bottom:2px">Contactez-nous :</div>
  <p class="body-txt" style="left:92px;top:166px;color:#fff;font-size:4.8px;line-height:1.9">Tél : 01 40 22 18 75<br>Fax : 01 40 22 18 76<br>Mail : contact@palme-vert.example</p>
  <p class="body-txt" style="right:14px;top:200px;color:#fff;font-size:4.8px">www.palme-vert.example &nbsp;|&nbsp; www.verdanta.example</p>
</section>

</body>
</html>
```